Broschüren-Design für Versicherungsagenten
Zielgruppe
Ich bin mit KL-Vorsorge als unabhängiger Versicherungsagent Selbstständig. (www.kl-vorsorge.de)
Ich habe mich auf die Absicherung von biometrischen Risiken spezialisiert - die auch in der Broschüre Thematisiert werden sollen. Das Oberthema der Broschüre ist 'biometrische Risiken'. Dies soll dann auf die Themen: Arbeitskraft, Langlebigkeit und Pflege heruntergebrochen werden.
Zielgruppe sind vor allem junge Menschen, die gerade erst eine Ausbildung gestartet oder ihr Studium beendet haben.
Aufgabenstellung
Das Design sollte die drei Hauptbereiche: Arbeitskraft, Langlebigkeit und Pflege, leicht verständlich dem Kunden veranschaulichen. Texte, Informationen und Grafiken (in der Reihenfolge, so wie ich mir das vorstelle) sind als Datei beigefügt.
Das ganze soll im DIN A4 Format gedruckt werden, wobei ich auf einen Hochwertigen Druck inklusive Druckveredelung hohen Wert lege.

```html
<!DOCTYPE html>
<html lang="de">
<head>
<meta charset="utf-8">
<title>KL-Vorsorge – Broschüre Biometrische Risiken</title>
<link href="https://fonts.googleapis.com/css2?family=Open+Sans:wght@400;600;700;800&display=swap" rel="stylesheet">
<style>
:root{
  --teal:#1a9c9c;
  --teal-dark:#137f80;
  --teal-light:#d3eeee;
  --ink:#333;
  --muted:#777;
  --ghost:#e4e4e4;
  --red:#e02a2a;
  --bg:#fff;
}
*{box-sizing:border-box;margin:0;padding:0}
html,body{width:1200px;height:4595px;overflow:hidden;background:var(--bg);font-family:"Open Sans",Arial,sans-serif;color:var(--ink)}
.canvas{position:relative;width:1200px;height:4595px}
.page{position:absolute;width:454px;height:638px;background:#fff;box-shadow:0 2px 10px rgba(0,0,0,.28);overflow:hidden}
.page > svg.deco{position:absolute;left:0;top:0;width:454px;height:638px}
.abs{position:absolute}
.tiny{font-size:5.6px;line-height:1.45;color:var(--muted)}
.small{font-size:7px;line-height:1.4;color:var(--ink)}
.label{font-size:8px;font-weight:700;color:var(--ink);line-height:1.3}
.h-teal{color:var(--teal);font-weight:700;font-size:25px;line-height:1.3}
.ghost{color:var(--ghost);font-weight:800;line-height:1.2}
.teal{color:var(--teal)}
.placeholder{position:absolute;background:#9a9a9a;border-radius:4px}
.cover-title{position:absolute;left:30px;top:14px;font-size:52px;font-weight:800;color:var(--ghost);line-height:1.25}
.brand{position:absolute;display:flex;align-items:center;gap:7px;font-weight:700;color:#fff;font-size:18px}
.brand i{display:block;width:26px;height:26px;border:2px solid #fff;border-radius:50%}
.pct{font-size:8px;color:var(--ink);text-align:center}
.bar{position:absolute;left:80px;width:294px;height:16px;border-radius:4px;background:#bdbdbd;font-size:5px;color:#fff;text-align:center;line-height:16px;font-weight:700}
.table{position:absolute;width:150px;height:78px;background:var(--teal-light);padding:8px;font-size:5px;line-height:1.6;color:#444}
</style>
</head>
<body>
<div class="canvas">

<!-- Cover -->
<section class="page" style="left:357px;top:130px;background:#f7f7f7">
  <div class="cover-title">Arbeitskraft<br>Langlebigkeit<br>Pflege</div>
  <svg class="deco" viewBox="0 0 454 638" aria-hidden="true">
    <polygon points="0,540 454,395 454,638 0,638" fill="var(--teal)"/>
    <circle cx="226" cy="362" r="150" fill="none" stroke="var(--teal)" stroke-width="14"/>
    <circle cx="226" cy="362" r="128" fill="none" stroke="var(--teal)" stroke-width="5"/>
    <circle cx="226" cy="362" r="170" fill="none" stroke="var(--teal)" stroke-width="3" stroke-dasharray="520 600"/>
    <circle cx="226" cy="362" r="112" fill="#fff"/>
  </svg>
  <div class="abs" role="img" aria-label="Foto: Läufer auf einer Straße im warmen Abendlicht" style="left:120px;top:256px;width:212px;height:212px;border-radius:50%;background:radial-gradient(circle at 45% 40%,#f3e0a8,#c6a15a 60%,#6d5630)"></div>
  <div class="brand" style="left:278px;top:556px"><i></i>KL-Vorsorge</div>
</section>

<!-- Row 1 left -->
<section class="page" style="left:104px;top:832px">
  <p class="abs tiny" style="left:38px;top:86px;width:200px">Viele Menschen sind bisher nur unzureichend oder gar nicht abgesichert. Dabei ist die Arbeitskraft die Basis für alle weiteren Ziele im Leben.</p>
  <p class="abs h-teal" style="left:38px;top:148px;width:380px">„Welche Versicherungen brauche ich denn wirklich?“</p>
  <p class="abs tiny" style="left:38px;top:210px;width:330px">Auf diese Frage gibt es eine klare Antwort: zuerst die Risiken, die Ihre Existenz bedrohen.</p>
  <p class="abs ghost" style="left:38px;top:258px;font-size:45px">Ihr<br>größtes<br>Vermögen<br>ist<br>Ihre<br>Arbeitskraft.</p>
  <p class="abs label" style="left:232px;top:268px;width:170px">Welchen physischen oder psychischen Belastungen sind Sie ausgesetzt?</p>
  <div class="placeholder" role="img" aria-label="Symbol: laufende Person" style="left:250px;top:318px;width:26px;height:44px;background:#c0c0c0"></div>
  <div class="placeholder" role="img" aria-label="Symbol: stehende Person" style="left:310px;top:318px;width:18px;height:44px"></div>
  <div class="placeholder" role="img" aria-label="Symbol: stehende Person" style="left:365px;top:318px;width:18px;height:44px"></div>
  <p class="abs pct" style="left:238px;top:370px;width:50px">21 %</p>
  <p class="abs pct" style="left:294px;top:370px;width:50px">7 %</p>
  <p class="abs pct" style="left:349px;top:370px;width:50px">15%</p>
  <p class="abs tiny" style="left:238px;top:382px;width:50px;text-align:center">Nerven und Psyche</p>
  <p class="abs tiny" style="left:294px;top:382px;width:50px;text-align:center">Unfälle</p>
  <p class="abs tiny" style="left:349px;top:382px;width:50px;text-align:center">Krebs</p>
  <div class="placeholder" role="img" aria-label="Symbol: Person" style="left:245px;top:428px;width:18px;height:44px"></div>
  <div class="placeholder" role="img" aria-label="Symbol: Person im Rollstuhl" style="left:300px;top:436px;width:30px;height:34px"></div>
  <div class="abs" role="img" aria-label="Symbol: Person" style="left:356px;top:432px;width:30px;height:30px;border-radius:50%;background:var(--teal)"></div>
  <p class="abs pct" style="left:238px;top:480px;width:50px">32 %</p>
  <p class="abs pct" style="left:294px;top:480px;width:50px">9 %</p>
  <p class="abs pct" style="left:349px;top:480px;width:50px">16 %</p>
  <p class="abs tiny" style="left:238px;top:492px;width:50px;text-align:center">Skelett und Bewegung</p>
  <p class="abs tiny" style="left:294px;top:492px;width:50px;text-align:center">Herz</p>
  <p class="abs tiny" style="left:349px;top:492px;width:50px;text-align:center">Sonstiges</p>
</section>

<!-- Row 1 right -->
<section class="page" style="left:609px;top:832px">
  <svg class="deco" viewBox="0 0 454 638" aria-hidden="true">
    <circle cx="350" cy="720" r="140" fill="none" stroke="var(--teal)" stroke-width="12"/>
    <circle cx="350" cy="720" r="118" fill="none" stroke="var(--teal)" stroke-width="4"/>
  </svg>
  <p class="abs label" style="left:28px;top:24px">Arbeitskraft<br><span style="font-weight:400">„Haben Sie ohne Arbeitskraft noch ein Einkommen?“</span></p>
  <p class="abs tiny" style="left:28px;top:64px;width:330px">Wer seine Arbeitskraft verliert, verliert sein Einkommen. Miete, Auto und Alltag laufen trotzdem weiter. Deshalb ist eine solide Absicherung so wichtig.</p>
  <p class="abs tiny" style="left:28px;top:118px;width:360px">Jeder vierte Arbeitnehmer muss seinen Beruf vorzeitig aufgeben, häufig aus psychischen Gründen oder wegen Erkrankungen des Bewegungsapparats.</p>
  <p class="abs tiny" style="left:28px;top:218px;width:140px">Statistisch wird einer von vier Menschen berufsunfähig, bevor er das Rentenalter erreicht.</p>
  <div class="placeholder" role="img" aria-label="Symbol: Person" style="left:218px;top:200px;width:20px;height:60px"></div>
  <div class="placeholder" role="img" aria-label="Symbol: Person" style="left:268px;top:200px;width:20px;height:60px"></div>
  <div class="placeholder" role="img" aria-label="Symbol: Person hervorgehoben" style="left:318px;top:200px;width:20px;height:60px;background:var(--teal)"></div>
  <div class="placeholder" role="img" aria-label="Symbol: Person" style="left:368px;top:200px;width:20px;height:60px"></div>
  <p class="abs h-teal" style="left:28px;top:276px;width:380px">Können Sie wissen<br>ob Sie einer der anderen<br>drei oder der EINE sind?</p>
  <p class="abs label" style="left:28px;top:428px">Staatliche Versorgung</p>
  <p class="abs tiny" style="left:28px;top:442px;width:340px">Der Staat zahlt nur eine Erwerbsminderungsrente. Diese greift erst, wenn Sie in keinem Beruf mehr arbeiten können, und ist meist sehr niedrig.</p>
  <p class="abs tiny" style="left:28px;top:494px;width:340px">Wer nach 2006 ins Berufsleben gestartet ist, hat keinen staatlichen Berufsschutz mehr.</p>
  <p class="abs tiny" style="left:28px;top:532px;width:380px">Daher ist private Vorsorge für junge Menschen besonders wichtig und heute günstig möglich.</p>
</section>

<!-- Row 2 left -->
<section class="page" style="left:104px;top:1566px">
  <p class="abs label" style="left:28px;top:42px;font-size:6.5px">Tägliche Arbeitsfähigkeit in irgendeiner Tätigkeit.</p>
  <p class="abs teal" style="left:22px;top:72px;width:130px;font-size:6px;text-align:center">&lt; unter 3 Stunden<br>Volle Erwerbsminderungsrente<br>ca. 30–35 % vom Bruttoeinkommen</p>
  <p class="abs teal" style="left:162px;top:72px;width:130px;font-size:6px;text-align:center">&gt; 3 – 6 Stunden<br>Halbe Erwerbsminderungsrente<br>ca. 15–17,5 % vom Bruttoeinkommen</p>
  <p class="abs teal" style="left:302px;top:72px;width:130px;font-size:6px;text-align:center">&gt; 6 Stunden und mehr<br>Keine Leistung</p>
  <p class="abs label" style="left:28px;top:132px;font-size:6.5px">Diese Versorgungslücke bedroht Ihre Existenz.</p>
  <p class="abs tiny" style="left:28px;top:142px;width:380px">Wovon leben Sie, wenn das Einkommen wegfällt und die Kosten bleiben?</p>
  <p class="abs h-teal" style="left:32px;top:200px;width:400px">Lösungen der<br>Absicherung Ihrer Arbeitskraft</p>
  <p class="abs tiny" style="left:32px;top:268px;width:250px">Es gibt verschiedene Wege, die Arbeitskraft abzusichern. Welche Lösung passt, hängt von Beruf, Gesundheit und Budget ab.</p>
  <div class="abs" role="img" aria-label="Symbol: Schirm" style="left:48px;top:350px;width:58px;height:58px;border-radius:50%;background:var(--teal)"></div>
  <div class="abs" role="img" aria-label="Symbol: Körper und Gesundheit" style="left:198px;top:350px;width:58px;height:58px;border-radius:50%;background:var(--teal)"></div>
  <div class="abs" role="img" aria-label="Symbol: Herzschlaglinie" style="left:348px;top:350px;width:58px;height:58px;border-radius:50%;background:var(--teal)"></div>
  <p class="abs tiny" style="left:26px;top:420px;width:120px"><b style="color:#444">Berufsunfähigkeitsversicherung – der Königsweg</b><br>Leistet, wenn Sie Ihren zuletzt ausgeübten Beruf zu mindestens 50 % nicht mehr ausüben können. Umfassender Schutz mit festen Beiträgen und garantierter Rente bis zum vereinbarten Endalter.</p>
  <p class="abs tiny" style="left:166px;top:420px;width:120px"><b style="color:#444">Schwere Krankheiten Vorsorge – Dread Disease</b><br>Zahlt eine Einmalsumme bei Diagnose schwerer Erkrankungen wie Krebs, Herzinfarkt oder Schlaganfall.</p>
  <p class="abs tiny" style="left:306px;top:420px;width:120px"><b style="color:#444">Grundfähigkeitsabsicherung – kein Ersatz</b><br>Leistet bei Verlust bestimmter Fähigkeiten wie Sehen, Gehen oder Greifen. Eine sinnvolle Alternative bei Vorerkrankungen.</p>
  <p class="abs tiny" style="left:70px;top:590px;width:320px;text-align:center">Wir finden gemeinsam die beste Absicherung Ihrer Arbeitskraft und beraten Sie unabhängig.</p>
</section>

<!-- Row 2 right -->
<section class="page" style="left:609px;top:1566px">
  <svg class="deco" viewBox="0 0 454 638" aria-hidden="true">
    <circle cx="520" cy="300" r="110" fill="none" stroke="var(--teal)" stroke-width="12"/>
    <circle cx="520" cy="300" r="90" fill="none" stroke="var(--teal)" stroke-width="4"/>
  </svg>
  <p class="abs label" style="left:24px;top:22px">Langlebigkeit<br><span style="font-weight:400">„Können Sie Ihr tägliches Leben noch selbst bewältigen?“</span></p>
  <p class="abs tiny" style="left:24px;top:62px;width:190px">In den letzten Jahrzehnten ist die Lebenserwartung stark gestiegen. Das Geld muss heute deutlich länger reichen.</p>
  <p class="abs h-teal" style="left:24px;top:142px">Reicht Ihnen<br>Ihre gesetzliche Rente?</p>
  <p class="abs tiny" style="left:24px;top:216px;width:220px"><b style="color:#444">Renteninformation</b><br>Brutto 1.700 € Rente mit 67, abzüglich Kranken- und Pflegeversicherung sowie Steuern.</p>
  <p class="abs tiny" style="left:24px;top:262px;width:220px"><b style="color:#444">Netto Rente &nbsp; 1.275 € Netto</b><br>Kaufkraft nach 10 Jahren 1.010 €, nach 20 Jahren 804 €.</p>
  <p class="abs teal" style="left:258px;top:236px;font-size:15px;font-weight:600;line-height:1.2">Lücke von<br>800 €/mtl.</p>
  <p class="abs ghost" style="left:24px;top:310px;font-size:40px">Den<br>Deutschen<br>droht</p>
  <p class="abs tiny" style="left:254px;top:330px;width:120px"><b style="color:#444">Können Sie sich als Rentner das leisten?</b><br>Lücke 500 € monatlich<br>Rente mit 67 ≈ 100.000 €<br>Rente mit 80 ≈ 160.000 €</p>
  <p class="abs tiny" style="left:24px;top:432px;width:180px"><b style="color:#444">Auszug aus dem Rentenbescheid der gesetzlichen Rentenversicherung</b></p>
  <p class="abs tiny" style="left:24px;top:470px;width:360px">Die Renten steigen langsamer als die Preise. Wer heute jung ist, muss mit einem deutlich niedrigeren Versorgungsniveau rechnen als die Generation der Eltern.</p>
  <p class="abs ghost" style="left:170px;top:520px;font-size:40px">Altersarmut.</p>
  <p class="abs tiny" style="left:24px;top:540px;width:130px">Mit Renteninformation zum Beratungsgespräch kommen.</p>
  <p class="abs teal" style="left:24px;top:596px;font-size:19px;font-weight:700">Hier ist Eigenverantwortung gefragt!</p>
</section>

<!-- Row 3 left -->
<section class="page" style="left:104px;top:2300px">
  <svg class="deco" viewBox="0 0 454 638" aria-hidden="true">
    <path d="M230,0 C330,0 420,30 454,60 L454,0 Z" fill="var(--teal)"/>
    <g stroke="#ccc" stroke-width="0.6">
      <line x1="70" y1="330" x2="240" y2="330"/><line x1="70" y1="310" x2="240" y2="310"/>
      <line x1="70" y1="290" x2="240" y2="290"/><line x1="70" y1="270" x2="240" y2="270"/>
      <line x1="70" y1="250" x2="240" y2="250"/>
    </g>
    <line x1="70" y1="250" x2="70" y2="330" stroke="#888" stroke-width="0.8"/>
    <line x1="70" y1="330" x2="240" y2="330" stroke="#888" stroke-width="0.8"/>
    <polyline points="70,328 110,322 150,310 190,290 230,262" fill="none" stroke="#f2b632" stroke-width="1.6"/>
    <polyline points="70,328 110,325 150,318 190,308 230,294" fill="none" stroke="#4cae4c" stroke-width="1.6"/>
    <polyline points="70,328 110,327 150,323 190,318 230,312" fill="none" stroke="#2f6fd0" stroke-width="1.6"/>
    <circle cx="64" cy="362" r="12" fill="#111"/><circle cx="134" cy="362" r="12" fill="#111"/><circle cx="204" cy="362" r="12" fill="#111"/>
    <text x="64" y="365" font-size="8" fill="#fff" text-anchor="middle" font-family="Open Sans" font-weight="700">20</text>
    <text x="134" y="365" font-size="8" fill="#fff" text-anchor="middle" font-family="Open Sans" font-weight="700">30</text>
    <text x="204" y="365" font-size="8" fill="#fff" text-anchor="middle" font-family="Open Sans" font-weight="700">40</text>
    <line x1="46" y1="380" x2="84" y2="380" stroke="#111" stroke-width="2"/>
    <line x1="116" y1="380" x2="154" y2="380" stroke="#111" stroke-width="2"/>
    <line x1="186" y1="380" x2="224" y2="380" stroke="#111" stroke-width="2"/>
    <line x1="210" y1="540" x2="236" y2="540" stroke="#333" stroke-width="1"/>
    <polyline points="231,536 236,540 231,544" fill="none" stroke="#333" stroke-width="1"/>
  </svg>
  <p class="abs label" style="left:30px;top:36px;font-size:7px">Anlagen in Fonds<br>solide Bausteine für die Altersvorsorge</p>
  <p class="abs tiny" style="left:30px;top:62px;width:120px">Fonds bieten langfristig gute Renditechancen. Schon kleine monatliche Beträge wachsen über viele Jahre zu einem beachtlichen Vermögen. Die Anlage ist flexibel, transparent und jederzeit anpassbar. Zinseszins arbeitet für Sie.</p>
  <div class="abs" role="img" aria-label="Schaubild: Sparbeiträge fließen über einen Fonds in verschiedene Anlagen" style="left:245px;top:70px;width:146px;height:214px;border-radius:14px;background:#8e8e8e"></div>
  <p class="abs label" style="left:30px;top:228px;font-size:6.5px">Das Zauberwort heißt Langfristigkeit.</p>
  <p class="abs tiny" style="left:252px;top:320px;width:150px"><b style="color:#444">Die Beispielrechnung</b><br>Monatlich 50 € Sparrate bis 67. Wer mit 20 beginnt, hat am Ende ein Vielfaches dessen, der erst mit 40 startet.</p>
  <p class="abs tiny" style="left:30px;top:400px;width:210px">Früh beginnen lohnt sich: Jedes Jahr zählt beim Vermögensaufbau.</p>
  <p class="abs tiny" style="left:30px;top:530px;width:170px">Lassen Sie uns gemeinsam einen Sparplan finden, der zu Ihrem Leben passt.</p>
  <p class="abs tiny" style="left:260px;top:530px;width:150px">Ab 25 € monatlich starten, jederzeit erhöhen oder pausieren.</p>
  <p class="abs tiny" style="left:30px;top:596px;width:380px">Wir erstellen Ihnen gerne ein individuelles Vorsorgekonzept mit den richtigen Fonds.</p>
</section>

<!-- Row 3 right -->
<section class="page" style="left:609px;top:2300px">
  <p class="abs label" style="left:46px;top:26px;font-weight:400">Pflege<br>„Können Sie sich alt werden auch finanziell leisten?“</p>
  <p class="abs tiny" style="left:46px;top:62px;width:300px">Die Zahl der Pflegebedürftigen in Deutschland steigt jedes Jahr. Pflege betrifft nicht nur ältere Menschen, sondern auch junge nach Unfall oder Krankheit.</p>
  <p class="abs ghost" style="left:44px;top:104px;font-size:32px">Pflegebedürftigkeit…<br>es kann<br>jeden treffen!</p>
  <div class="abs" style="left:312px;top:182px;width:124px;height:124px;border-radius:50%;background:var(--teal);border:3px solid #fff;box-shadow:0 0 0 3px var(--teal);color:#fff;font-size:6px;text-align:center;padding:28px 14px;line-height:1.4"><b style="font-size:7px">25 Menschen</b><br>werden alle 60 Minuten in Deutschland pflegebedürftig – jeden Tag, rund um die Uhr.</div>
  <p class="abs label" style="left:46px;top:282px;font-size:7px">Staatliche Versorgung – teilweise im Pflegefall</p>
  <p class="abs tiny" style="left:46px;top:296px;width:300px">Die gesetzliche Pflegeversicherung ist nur eine Teilkaskoversicherung. Den Rest zahlen Sie selbst oder Ihre Angehörigen.</p>
  <div class="table" style="left:46px;top:370px"><b>Ausgangspunkt: Pflegegrad 3</b><br>Kosten Pflegeheim 3.400 €<br>Leistung Pflegekasse 1.262 €<br>Eigenanteil 2.138 €<br><span style="color:var(--red)">Lücke monatlich</span></div>
  <div class="table" style="left:214px;top:370px"><b>Ausgangspunkt: Pflegegrad 5</b><br>Kosten Pflegeheim 4.100 €<br>Leistung Pflegekasse 2.005 €<br>Eigenanteil 2.095 €<br><span style="color:var(--red)">Lücke monatlich</span></div>
  <p class="abs tiny" style="left:46px;top:484px">Können Sie sich das leisten?</p>
  <p class="abs tiny" style="left:46px;top:520px;width:320px">Die Kosten der Pflege übersteigen oft Rente und Ersparnisse. Dann haften Kinder oder das eigene Vermögen.</p>
</section>

<!-- Row 4 left -->
<section class="page" style="left:104px;top:3036px">
  <p class="abs tiny" style="left:80px;top:30px;width:294px;text-align:center"><b style="color:#444">Wer zahlt?</b><br>Die Reihenfolge, in der die Pflegekosten übernommen werden.</p>
  <div class="bar" style="top:76px;background:#9e9e9e">Leistungen der Pflegeversicherung</div>
  <div class="bar" style="top:106px">Eigenes Einkommen</div>
  <div class="bar" style="top:136px">Eigenes Vermögen</div>
  <div class="bar" style="top:166px;background:var(--red)">Unterhalt durch Kinder und Sozialamt</div>
  <p class="abs label" style="left:60px;top:236px;font-size:6.5px">Vollkasko nur mit Pflegezusatz</p>
  <p class="abs tiny" style="left:60px;top:250px;width:300px">Eine private Pflegezusatzversicherung schließt die Lücke. Je früher Sie abschließen, desto günstiger sind die Beiträge und Gesundheitsfragen sind einfacher.</p>
  <p class="abs h-teal" style="left:60px;top:340px">Eines bleibt aber gleich:</p>
  <p class="abs tiny" style="left:60px;top:378px;width:300px">Die gesetzliche Pflegeversicherung reicht allein nicht aus.</p>
  <p class="abs tiny" style="left:60px;top:396px;width:300px">Wir finden mit Ihnen die passende Pflegevorsorge.</p>
</section>

<!-- Row 4 right -->
<section class="page" style="left:609px;top:3036px">
  <svg class="deco" viewBox="0 0 454 638" aria-hidden="true">
    <circle cx="120" cy="720" r="140" fill="none" stroke="var(--teal)" stroke-width="12"/>
    <circle cx="120" cy="720" r="118" fill="none" stroke="var(--teal)" stroke-width="4"/>
  </svg>
  <p class="abs h-teal" style="left:44px;top:50px">Wir stehen für:<br>TOP Bedingungen<br>den besten<br>Versicherungsschutz</p>
  <p class="abs tiny" style="left:44px;top:196px;width:320px">Als unabhängiger Versicherungsagent vergleiche ich für Sie den gesamten Markt und wähle nur Tarife mit erstklassigen Bedingungen aus.</p>
  <p class="abs tiny" style="left:44px;top:232px;width:320px">Ich begleite Sie persönlich – vom ersten Gespräch bis zum Leistungsfall.</p>
  <p class="abs tiny" style="left:44px;top:258px;width:320px">Transparente Beratung, faire Beiträge und ein Ansprechpartner für alle Fragen.</p>
  <p class="abs tiny" style="left:44px;top:310px;width:320px">Haben Sie Fragen zu Ihrer Vorsorge? Oder möchten Sie ein Beratungsgespräch vereinbaren?</p>
</section>

<!-- Back cover -->
<section class="page" style="left:348px;top:3762px">
  <svg class="deco" viewBox="0 0 454 638" aria-hidden="true">
    <polygon points="0,0 454,0 454,250 0,110" fill="var(--teal)"/>
    <circle cx="227" cy="300" r="170" fill="none" stroke="var(--teal)" stroke-width="3" stroke-dasharray="560 600"/>
    <circle cx="227" cy="300" r="150" fill="none" stroke="var(--teal)" stroke-width="14"/>
    <circle cx="227" cy="300" r="128" fill="none" stroke="var(--teal)" stroke-width="5"/>
    <circle cx="227" cy="300" r="115" fill="#fff"/>
  </svg>
  <p class="abs tiny" style="left:127px;top:270px;width:200px;text-align:center;color:#555">Max Belwig<br>KL-Vorsorge<br>Lindenweg 12<br>70173 Stuttgart<br>Tel. 0711 555 0142<br>info@kl-vorsorge.de · www.kl-vorsorge.de</p>
</section>

</div>
</body>
</html>
```